Business card design needed for rebranded top-end landscaping business

We need a new business card design, incorporating our logo (colours Green #8dc63f and Grey #8a8c8e) and also some options that include the colour dark navy (eg #000040) as our uniforms are navy with white and grey trim.

We are an innovative landscaping company that maintains high-end gardens for meticulous clients. We pride ourselves on our customer service, our professionalism, and our workmanship.

Our business name needs to be easily read and our branding needs to be bold and memorable, without screaming "tradesman"! We prefer clean lines over lots of fine detail.

The design MUST include:
- Business name ("Brindlemere Gardening")
- Logo (file uploaded)
- Employee name
- Phone number
- Email address
- www.brindlemeregardening.com.au
- Facebook & Instagram logos
- The Turfcraft Guild logo (file uploaded) along with the word "Member"
- Licence "Lic. 871396K"

OPTIONAL inclusions:
- "Creating outdoor spaces for our community to be inspired, refreshed and re-energised"
- "Landscape Maintenance - Irrigation - Arboriculture" (dashes can be replaced with dots or other)
- "Fully qualified, licensed & insured"
- "Residential - Strata - Commercial - Real Estate" (dashes can be replaced with dots or other)

Target Market(s)

High-end professionals and retirees, real estate agents

Industry/Entity Type

Landscaping

Contact Information for Business Card

See Project description

Font styles to use
Sans Serif

Colors

Designer to choose colors to be used in the design.

Requirements
Must have
• Must incorporate our logo, and colours Green #8dc63f and Grey #8a8c8e) from the logo, and the colour DARK NAVY (eg #000040).
• The design MUST include:
• - Business name ("Brindlemere Gardening")
• - Logo (file uploaded)
• - Employee name
• - Phone number
• - Email address
• - www.brindlemeregardening.com.au
• - Facebook & Instagram logos
• - The Turfcraft Guild logo (file uploaded) along with the word "Member"
• - Licence "Lic. 871396K"
Nice to have
• OPTIONAL inclusions:
• - "Creating outdoor spaces for our community to be inspired, refreshed and re-energised"
• - "Landscape Maintenance - Irrigation - Arboriculture" (dashes can be replaced with dots or other)
• - "Fully qualified, licensed & insured"
• - "Residential - Strata - Commercial - Real Estate" (dashes can be replaced with dots or other)

```html
<!DOCTYPE html>
<html lang="en">
<head>
<meta charset="utf-8">
<title>Brindlemere Gardening – Business Card</title>
<link href="https://fonts.googleapis.com/css2?family=Tinos:wght@400;700&display=swap" rel="stylesheet">
<style>
  :root {
    --navy: #000040;
    --navy-light: #0a0a7a;
    --navy-mid: #040458;
    --green: #8dc63f;
    --grey: #8a8c8e;
    --silver: #c9cbcd;
    --white: #ffffff;
    --backdrop: #e4e4e4;
  }
  * { box-sizing: border-box; margin: 0; padding: 0; }
  html, body { width: 1200px; height: 960px; overflow: hidden; }
  body {
    background: var(--backdrop);
    font-family: "Tinos", "Times New Roman", serif;
    display: flex;
    flex-direction: column;
    align-items: center;
    justify-content: center;
    gap: 60px;
  }
  .card {
    position: relative;
    width: 640px;
    height: 366px;
    border-radius: 22px;
    overflow: hidden;
    background: linear-gradient(135deg, var(--navy-light) 0%, var(--navy-mid) 45%, var(--navy) 100%);
    box-shadow: 0 14px 30px rgba(0,0,0,0.25);
    color: var(--white);
  }

  /* Front */
  .member-badge {
    position: absolute;
    top: 24px;
    right: 30px;
    width: 54px;
    height: 34px;
    border: 1.5px solid var(--silver);
    border-radius: 4px;
    opacity: 0.85;
  }
  .brand {
    display: flex;
    align-items: center;
    gap: 14px;
  }
  .brand-mark {
    width: 44px;
    height: 44px;
    border-radius: 50%;
    flex: none;
  }
  .brand-name {
    font-weight: 700;
    font-size: 34px;
    letter-spacing: 0.3px;
    line-height: 1;
  }
  .front .brand {
    position: absolute;
    top: 140px;
    left: 0;
    right: 0;
    justify-content: center;
  }
  .front .brand-mark { background: var(--silver); }
  .front .brand-name { color: var(--silver); }
  .services {
    position: absolute;
    bottom: 62px;
    left: 0;
    right: 0;
    text-align: center;
    font-size: 17px;
    color: var(--white);
    letter-spacing: 0.2px;
  }
  .services .dot {
    display: inline-block;
    width: 7px;
    height: 7px;
    border-radius: 50%;
    background: var(--green);
    margin: 0 8px 2px;
    vertical-align: middle;
  }

  /* Back */
  .back .brand {
    position: absolute;
    top: 150px;
    left: 36px;
    flex-direction: column;
    align-items: center;
    gap: 12px;
    width: 240px;
  }
  .back .brand-mark { background: var(--green); }
  .back .brand-name {
    color: var(--grey);
    font-size: 28px;
    text-align: center;
    line-height: 1.1;
  }
  .divider {
    position: absolute;
    left: 300px;
    top: 96px;
    width: 1px;
    height: 150px;
    background: var(--grey);
  }
  .social {
    position: absolute;
    top: 22px;
    right: 24px;
    display: flex;
    gap: 6px;
  }
  .social span {
    width: 20px;
    height: 20px;
    border-radius: 50%;
    background: var(--green);
  }
  .contact {
    position: absolute;
    left: 322px;
    top: 96px;
    right: 20px;
  }
  .person-name {
    color: var(--green);
    font-weight: 700;
    font-size: 24px;
    line-height: 1.1;
  }
  .person-role {
    color: var(--grey);
    font-size: 15px;
    margin: 2px 0 10px 14px;
  }
  .contact-list { list-style: none; margin-left: 14px; }
  .contact-list li {
    display: flex;
    align-items: center;
    gap: 7px;
    font-size: 14.5px;
    color: var(--silver);
    line-height: 1.45;
    white-space: nowrap;
  }
  .contact-list svg { width: 12px; height: 12px; flex: none; fill: var(--white); }
  .licence {
    margin: 12px 0 0 14px;
    font-size: 16px;
    color: var(--silver);
  }
  .accent-band {
    position: absolute;
    left: 0;
    right: 0;
    bottom: 0;
    height: 14px;
    background: var(--green);
  }
</style>
</head>
<body>

  <section class="card front" aria-label="Business card front">
    <div class="member-badge" aria-label="The Turfcraft Guild member badge"></div>
    <div class="brand">
      <span class="brand-mark"></span>
      <span class="brand-name">Brindlemere Gardening</span>
    </div>
    <p class="services">Residential<span class="dot"></span>Strata<span class="dot"></span>Commercial<span class="dot"></span>Real Estate</p>
  </section>

  <section class="card back" aria-label="Business card back">
    <div class="social" aria-label="Social media">
      <span></span><span></span>
    </div>
    <div class="brand">
      <span class="brand-mark"></span>
      <span class="brand-name">Brindlemere Gardening</span>
    </div>
    <div class="divider"></div>
    <div class="contact">
      <p class="person-name">Daniel Hartley</p>
      <p class="person-role">President</p>
      <ul class="contact-list">
        <li>
          <svg viewBox="0 0 24 24" aria-hidden="true"><path d="M6.6 10.8a15.1 15.1 0 0 0 6.6 6.6l2.2-2.2a1 1 0 0 1 1-.25 11.4 11.4 0 0 0 3.6.57 1 1 0 0 1 1 1V20a1 1 0 0 1-1 1A17 17 0 0 1 3 4a1 1 0 0 1 1-1h3.5a1 1 0 0 1 1 1c0 1.25.2 2.45.57 3.6a1 1 0 0 1-.25 1z"/></svg>
          369-482-1057
        </li>
        <li>
          <svg viewBox="0 0 24 24" aria-hidden="true"><path d="M2 5h20v14H2z M4 7v.5l8 5 8-5V7l-8 5z" fill-rule="evenodd"/></svg>
          info@brindlemeregardening.com.au
        </li>
        <li>
          <svg viewBox="0 0 24 24" aria-hidden="true"><path d="M12 2a10 10 0 1 0 0 20 10 10 0 0 0 0-20zm0 2c.9 0 2.2 2 2.7 5H9.3C9.8 6 11.1 4 12 4zm-7.4 7h3.5a18 18 0 0 0 0 2H4.6a8 8 0 0 1 0-2zm5 0h4.8a16 16 0 0 1 0 2H9.6a16 16 0 0 1 0-2zm6.3 0h3.5a8 8 0 0 1 0 2h-3.5a18 18 0 0 0 0-2zM9.3 15h5.4c-.5 3-1.8 5-2.7 5s-2.2-2-2.7-5z"/></svg>
          www.brindlemeregardening.com.au
        </li>
      </ul>
      <p class="licence">Lic. 871396K</p>
    </div>
    <div class="accent-band"></div>
  </section>

</body>
</html>
```